Software Company Business Card

We are looking for a new design of our business card. The design will also be used in the rest of our branding and marketing materials as we want to keep it all uniform. We sell POS software to fine/luxury jewelers and also offer other business services as well to help the jeweler manage their business and need something more updated, technical and fresh, preferably more on the masculine side. We do not want any designs with gems in them but if possible would like to incorporate the circle and arrow in the logo into the design, but not a requirement if you can't make it work. I would like to see a variety of the mix. The colors need to remain our blue and orange and the logo can not change. The squiggly lines have been used as our corporate identity for over 20 years and its time to update. Our company name is PELK (Bright Ledger Counter Solutions).

Target Market(s)

High End Jewelers

Industry/Entity Type

Software

Contact Information for Business Card

Requirements
Must have
• Our logo and the colors must remain the same. Blue is #d95d39 and Orange is #0f5682.
Nice to have
• The circle and arrow incorporated but not a requirement.
Should not have
• Anything jewelry or gem related.

```html
<!DOCTYPE html>
<html lang="en">
<head>
<meta charset="utf-8">
<title>PELK Business Card</title>
<link rel="stylesheet" href="https://fonts.googleapis.com/css2?family=Arimo:wght@400;700&family=PT+Sans:wght@700&display=swap">
<style>
  :root {
    --brand-blue: #115786;
    --brand-orange: #d95d39;
    --ink: #222222;
    --rule: #555555;
    --paper: #ffffff;
    --backdrop: #2a2a2a;
  }
  * { margin: 0; padding: 0; box-sizing: border-box; }
  html, body { width: 1200px; height: 900px; overflow: hidden; }
  body {
    background: var(--backdrop);
    font-family: "Arimo", Arial, sans-serif;
    position: relative;
  }
  .card {
    position: absolute;
    width: 560px;
    height: 320px;
    box-shadow: 0 12px 30px rgba(0,0,0,0.5);
  }
  .card-front {
    left: 110px; top: 100px;
    background: var(--paper);
    border-bottom: 4px solid var(--brand-blue);
  }
  .card-back {
    left: 530px; top: 480px;
    background: var(--brand-blue);
    display: flex;
    align-items: center;
    justify-content: center;
  }
  .identity {
    position: absolute;
    left: 190px; top: 88px;
  }
  .person-name {
    font-family: "PT Sans", Arial, sans-serif;
    font-weight: 700;
    font-size: 27px;
    color: var(--brand-blue);
    line-height: 1;
  }
  .person-title {
    font-size: 15px;
    color: var(--brand-orange);
    margin-top: 3px;
  }
  .address {
    position: absolute;
    right: 282px; top: 152px;
    text-align: right;
    font-style: normal;
    font-size: 14.5px;
    line-height: 19px;
    color: var(--ink);
  }
  .divider {
    position: absolute;
    left: 290px; top: 146px;
    width: 1px; height: 86px;
    background: var(--rule);
  }
  .contacts {
    position: absolute;
    left: 302px; top: 150px;
    list-style: none;
    font-size: 14px;
    line-height: 20px;
    color: var(--ink);
  }
  .contacts li { display: flex; align-items: center; gap: 7px; }
  .contacts svg { width: 13px; height: 13px; fill: var(--brand-blue); flex: none; }
  .web-name { color: var(--brand-blue); }
  .logo-word {
    font-family: "Arimo", Arial, sans-serif;
    font-weight: 700;
    font-size: 84px;
    line-height: 1;
    color: var(--paper);
    letter-spacing: -1px;
  }
</style>
</head>
<body>
  <section class="card card-front">
    <div class="identity">
      <p class="person-name">Dorian Vessel</p>
      <p class="person-title">Director of Global Operations</p>
    </div>
    <address class="address">
      1480 Harbor Point<br>Drive Suite 210<br>Henderson<br>NV 89052,USA
    </address>
    <div class="divider"></div>
    <ul class="contacts">
      <li>
        <svg viewBox="0 0 16 16" aria-hidden="true"><path d="M3.5 1.5l2.5 0 1.2 3.2-1.6 1.2a9 9 0 0 0 4.5 4.5l1.2-1.6 3.2 1.2v2.5c0 .8-.7 1.5-1.5 1.5A12.5 12.5 0 0 1 2 3c0-.8.7-1.5 1.5-1.5z"/></svg>
        + 800 555-0147
      </li>
      <li>
        <svg viewBox="0 0 16 16" aria-hidden="true"><rect x="4" y="1" width="8" height="4"/><rect x="1" y="6" width="14" height="6" rx="1"/><rect x="4" y="10" width="8" height="5"/></svg>
        +1 702 555-0182
      </li>
      <li>
        <svg viewBox="0 0 16 16" aria-hidden="true"><path d="M1 3h14v10H1z M1.5 3.5L8 9l6.5-5.5" stroke="#fff" stroke-width="1"/></svg>
        dorian@pelkledger.com
      </li>
      <li>
        <svg viewBox="0 0 16 16" aria-hidden="true"><circle cx="8" cy="8" r="7"/><path d="M1 8h14M8 1c-3 3.5-3 10.5 0 14M8 1c3 3.5 3 10.5 0 14M2.5 4.5h11M2.5 11.5h11" stroke="#fff" stroke-width="0.9" fill="none"/></svg>
        <span>www.<span class="web-name">pelkledger</span>.com</span>
      </li>
    </ul>
  </section>

  <section class="card card-back">
    <span class="logo-word">PELK</span>
  </section>
</body>
</html>
```